Catering company looking to promote business

We need a flyer design for our company named "Berry Good Bites." We cater/deliver açaí bowls and smoothies.

The objective of this flyer is to let companies know that we are taking açaí bowls and smoothie orders and they can be delivered to them.

Some key points we would like on the flyer:
- Photo of açaí bowl and smoothie
- Menu w/ pricing
- "No hidden delivery fees"
- 5 bowl or smoothie minimum
- Online ordering through website:
https://shopkiosk.example/store/berrygoodbites
- For the month of February --> Get one free topping and drizzle!
- FRIDAY DELIVERIES ONLY
- Questions? Call (555) 417-9832
- social media chatterbook & snapgram @bgbites
- website www.berrygoodbites.example

font - hello beautiful

Target Market(s)

Juice, smoothies, açaí bowls

Industry/Entity Type

Business

Font styles to use
Other font styles liked:
• Hello Beautiful

Colors
a64599
b768aa
d3a5cc
eedced
f7f1f7
9bcb3c

Requirements
Must have
• Please match logo, fonts, color schemes, etc.

```html
<!DOCTYPE html>
<html lang="en">
<head>
<meta charset="utf-8">
<title>Berry Good Bites – Delivery Flyer</title>
<link rel="stylesheet" href="https://fonts.googleapis.com/css2?family=Caveat+Brush&family=Montserrat:wght@400;600;700&display=swap">
<style>
:root{
  --plum:#a64599;
  --orchid:#b768aa;
  --lilac:#d3a5cc;
  --blush:#eedced;
  --mist:#f7f1f7;
  --lime:#9bcb3c;
  --ink:#3a3a3a;
  --stage:#ece8ea;
}
*{box-sizing:border-box;margin:0;padding:0}
html,body{width:1200px;height:1000px;overflow:hidden;background:var(--stage)}
body{font-family:"Montserrat",Arial,sans-serif;color:var(--ink);position:relative}
.flyer{position:absolute;top:150px;width:500px;height:700px;background:linear-gradient(160deg,#fff 0%,var(--mist) 60%,#f1f7e8 100%);overflow:hidden;box-shadow:0 6px 18px rgba(0,0,0,.18)}
.flyer--front{left:70px}
.flyer--back{left:630px}
.flyer__shapes{position:absolute;inset:0}
.brush{font-family:"Caveat Brush",cursive}
.logo{position:absolute;display:flex;align-items:center;gap:10px}
.logo__dot{width:20px;height:20px;border-radius:50%;background:var(--lime)}
.logo__name{font-family:"Caveat Brush",cursive;color:var(--plum);font-size:36px;line-height:1;white-space:nowrap}
.promo-band{position:absolute;left:0;right:0;bottom:0;height:36px;background:var(--lime);color:#fff;font-weight:700;font-size:11px;letter-spacing:.3px;display:flex;align-items:center;justify-content:center;white-space:nowrap}
.social{display:flex;align-items:center;gap:5px;font-size:11px;font-weight:600}
.social__box{width:15px;height:15px;background:var(--orchid);border-radius:3px}
.phone{font-family:"Caveat Brush",cursive;color:var(--lime);font-size:40px;line-height:1;white-space:nowrap}
.small-caps{font-size:11px;font-weight:700;letter-spacing:.4px}

/* front */
.front-info{position:absolute;right:28px;top:518px;text-align:right}
.front-info__fees{color:var(--plum);font-weight:700;font-size:16px;line-height:1.2}
.front-info__min{font-size:13px;margin-top:2px}
.front-info__order{font-size:12px;font-weight:600;margin-top:5px}
.front-info__url{color:var(--lime);font-weight:700;font-size:12px;margin-top:2px}
.front-info__friday{margin-top:5px}
.front-contact{position:absolute;left:28px;right:28px;bottom:46px;display:flex;align-items:flex-end;justify-content:space-between}
.front-contact__left{display:flex;flex-direction:column;gap:6px}

/* back */
.bowl{position:absolute;left:36px;top:110px;width:225px}
.bowl__title{color:var(--lime);font-size:38px;line-height:1;white-space:nowrap}
.bowl__price{color:var(--plum);font-family:"Montserrat",sans-serif;font-size:13px;font-weight:600;margin-left:4px}
.bowl__desc{font-size:12px;line-height:1.4;margin-top:6px}
.extra{position:absolute;left:36px;top:330px;color:var(--lime);font-size:26px;line-height:1;white-space:nowrap}
.menu{position:absolute;left:36px;right:28px;top:372px;list-style:none}
.menu__row{display:flex;gap:12px;margin-bottom:8px}
.menu__label{width:112px;flex:none;color:var(--lime);font-family:"Caveat Brush",cursive;font-size:28px;line-height:1}
.menu__price{display:block;color:var(--plum);font-family:"Montserrat",sans-serif;font-size:11px;font-weight:600}
.menu__items{color:var(--plum);font-family:"Caveat Brush",cursive;font-size:18px;line-height:1.15;padding-top:4px}
.back-contact{position:absolute;left:36px;right:28px;bottom:46px;display:flex;align-items:flex-end;justify-content:space-between}
.back-contact__left{display:flex;flex-direction:column;gap:4px}
.back-contact__friday{font-size:9px}
</style>
</head>
<body>

<section class="flyer flyer--front">
  <svg class="flyer__shapes" viewBox="0 0 500 700">
    <defs>
      <linearGradient id="bowlPhoto" x1="0" y1="0" x2="1" y2="1">
        <stop offset="0" stop-color="#c9a27e"/>
        <stop offset=".45" stop-color="#e0485a"/>
        <stop offset="1" stop-color="#5b2a4a"/>
      </linearGradient>
    </defs>
    <path role="img" aria-label="Photo of an açaí bowl topped with strawberries, blueberries and granola" d="M0 0H500V330C360 360 170 290 0 90Z" fill="url(#bowlPhoto)"/>
    <g fill="none">
      <path d="M0 190C170 390 360 450 500 430" stroke="var(--blush)" stroke-width="40"/>
      <path d="M0 160C170 360 360 420 500 400" stroke="var(--lilac)" stroke-width="30"/>
      <path d="M0 130C170 330 360 390 500 370" stroke="var(--orchid)" stroke-width="30"/>
      <path d="M0 100C170 300 360 360 500 340" stroke="var(--plum)" stroke-width="30"/>
    </g>
  </svg>

  <div class="logo" style="left:28px;top:470px">
    <span class="logo__dot"></span>
    <span class="logo__name">Berry Good Bites</span>
  </div>

  <div class="front-info">
    <p class="front-info__fees">“No Hidden Delivery Fees”</p>
    <p class="front-info__min">5 Bowl Or Smoothie Minimum</p>
    <p class="front-info__order">ONLINE ORDERING THROUGH WEBSITE:</p>
    <p class="front-info__url">https://shopkiosk.example/store/berrygoodbites</p>
    <p class="front-info__friday small-caps">FRIDAY DELIVERIES ONLY</p>
  </div>

  <div class="front-contact">
    <div class="front-contact__left">
      <p class="small-caps">QUESTIONS? CALL</p>
      <div class="social"><span class="social__box"></span><span class="social__box"></span><span class="social__box"></span><span>@bgbites</span></div>
    </div>
    <p class="phone">(555) 417-9832</p>
  </div>

  <p class="promo-band">FOR THE MONTH OF FEBRUARY - GET ONE FREE TOPPING AND DRIZZLE!</p>
</section>

<section class="flyer flyer--back">
  <svg class="flyer__shapes" viewBox="0 0 500 700">
    <defs>
      <linearGradient id="smoothiePhoto" x1="0" y1="0" x2="1" y2="1">
        <stop offset="0" stop-color="#f4f1ef"/>
        <stop offset=".55" stop-color="#e2dcda"/>
        <stop offset="1" stop-color="#8a2c4a"/>
      </linearGradient>
    </defs>
    <g fill="none">
      <path d="M250 0C230 200 330 350 500 470" stroke="var(--blush)" stroke-width="40"/>
      <path d="M275 0C255 200 350 340 500 445" stroke="var(--lilac)" stroke-width="28"/>
      <path d="M300 0C280 195 370 325 500 420" stroke="var(--orchid)" stroke-width="28"/>
      <path d="M325 0C305 190 390 310 500 395" stroke="var(--plum)" stroke-width="28"/>
    </g>
    <path role="img" aria-label="Photo of a hand holding a berry smoothie cup with a straw" d="M338 0H500V385C400 310 320 200 338 0Z" fill="url(#smoothiePhoto)"/>
  </svg>

  <div class="logo" style="left:30px;top:40px">
    <span class="logo__dot"></span>
    <span class="logo__name">Berry Good Bites</span>
  </div>

  <div class="bowl">
    <p class="bowl__title brush">AÇAÍ BOWL<span class="bowl__price">$9.00</span></p>
    <p class="bowl__desc">Acai Sorbet Topped With Granola, Bananas, Strawberries, Blueberries, Coconut Shavings And Drizzled With Honey</p>
  </div>

  <p class="extra brush">WANT TO ADD SOMETHING EXTRA?</p>

  <ul class="menu">
    <li class="menu__row">
      <span class="menu__label">FRUITS<span class="menu__price">$1.00</span></span>
      <span class="menu__items">BANANAS, STRAWBERRIES, BLUEBERRIES</span>
    </li>
    <li class="menu__row">
      <span class="menu__label">TOPPINGS<span class="menu__price">.50¢</span></span>
      <span class="menu__items">ALMONDS, CHIA SEEDS, HEMP SEEDS, CACAO NIBS, QUINOA PUFFS, COCONUT SHAVINGS, GRANOLA</span>
    </li>
    <li class="menu__row">
      <span class="menu__label">DRIZZLE<span class="menu__price">.50¢</span></span>
      <span class="menu__items">PEANUT BUTTER, ALMOND BUTTER, HONEY, AGAVE</span>
    </li>
  </ul>

  <div class="back-contact">
    <div class="back-contact__left">
      <div class="social"><span class="social__box"></span><span class="social__box"></span><span class="social__box"></span><span>@bgbites</span></div>
      <p class="small-caps">QUESTIONS? CALL</p>
      <p class="small-caps back-contact__friday">FRIDAY DELIVERIES ONLY</p>
    </div>
    <p class="phone">(555) 417-9832</p>
  </div>

  <p class="promo-band">FOR THE MONTH OF FEBRUARY - GET ONE FREE TOPPING AND DRIZZLE!</p>
</section>

</body>
</html>
```